Pub/Bar snack and nibbles packaging

What we want:
We require professional packaging design for our jerky range.

About us and why we're here:
We're a husband and wife team from a small town who has been supplying artesian dried meats to local pubs/bars in outback Australia. Through word of mouth our volume has been growing steadily these few years. We seek someone who can assist provide a packaging range that best represents what great products my wife and I have been producing. And ultimately, a packaging that this product deserves. We have attached pictures of bar/pubs to give an idea of where our product is typically placed.

Target Market(s)

Target market:
Our customers are patrons of country motels / pubs and convenience stores. Our jerky goes particularly well with a cold beer.

Industry/Entity Type

It Professional

Requirements
Must have
• Specifics:
• Business Name: Gumridge Meats. Artisan Style.
• Product: Beef Chunks (we have 4 different flavours original, spicy, honey, pepper. The design should be easily changeable to accomodate different flavours)
• Description: Made from 100% Australian Beef
• Typography: We have attached some fonts for inspiration (e.g., lazy falcon, other alcohol brands)
• Packet Size: 110mm (w) x 170mm (l)
• We also require the back of the packaging designed as well. That information will be provided to the winning designer chosen.
Nice to have
• Design Concept:
• The design should tell a story which features an outback or bush setting. We have provided a few examples for inspiration (e.g., jackaroo walking with working dog, on a horse, swagman camping) or come up with your own. We will decide the final design based on the story that we can most related to.
Should not have
• We do not want any photo images on this design, illustrations and text only.

```html
<!DOCTYPE html>
<html lang="en">
<head>
<meta charset="utf-8">
<title>Gumridge Meats – Honey Beef Chunks</title>
<link rel="stylesheet" href="https://fonts.googleapis.com/css2?family=Alfa+Slab+One&family=Bitter:ital,wght@0,400;0,700;1,700&display=swap">
<style>
  :root {
    --pack-yellow: #ffcd05;
    --bark-brown: #5b3010;
    --bark-soft: #7a4a1c;
  }
  html, body {
    margin: 0;
    padding: 0;
    overflow: hidden;
    background: var(--pack-yellow);
  }
  .pack-front {
    position: relative;
    width: 777px;
    height: 1200px;
    background: var(--pack-yellow);
    color: var(--bark-brown);
    overflow: hidden;
  }
  .brand-name {
    position: absolute;
    left: 0;
    top: 0;
    width: 777px;
    height: 400px;
  }
  .brand-name text {
    font-family: "Alfa Slab One", "Rockwell", serif;
    fill: var(--bark-brown);
    font-size: 138px;
  }
  .double-rule {
    position: absolute;
    left: 48px;
    width: 691px;
    height: 17px;
    border-top: 5px solid var(--bark-brown);
    border-bottom: 5px solid var(--bark-brown);
    box-sizing: border-box;
  }
  .rule-top { top: 419px; }
  .rule-mid { top: 1035px; }
  .rule-bottom { top: 1121px; }
  .tagline {
    position: absolute;
    top: 476px;
    width: 100%;
    text-align: center;
    margin: 0;
    font-family: "Bitter", "Georgia", serif;
    font-style: italic;
    font-weight: 700;
    font-size: 38px;
  }
  .bush-scene {
    position: absolute;
    left: 130px;
    top: 580px;
    width: 517px;
    height: 340px;
    border-radius: 48% 48% 18px 18px / 42% 42% 18px 18px;
    background: linear-gradient(180deg, var(--bark-brown) 0%, var(--bark-soft) 100%);
  }
  .flavour {
    position: absolute;
    top: 962px;
    width: 100%;
    text-align: center;
    margin: 0;
    font-family: "Bitter", "Georgia", serif;
    font-weight: 700;
    font-size: 31px;
  }
  .origin {
    position: absolute;
    top: 1068px;
    width: 100%;
    text-align: center;
    margin: 0;
    font-family: "Bitter", "Georgia", serif;
    font-weight: 400;
    font-size: 30px;
  }
</style>
</head>
<body>
  <main class="pack-front">
    <svg class="brand-name" viewBox="0 0 777 400" aria-label="Gumridge Meats">
      <text x="388.5" y="221" text-anchor="middle" textLength="466" lengthAdjust="spacingAndGlyphs">Gumridge</text>
      <text x="388.5" y="362" text-anchor="middle" textLength="230" lengthAdjust="spacingAndGlyphs">Meats</text>
    </svg>

    <div class="double-rule rule-top"></div>

    <p class="tagline">Artisan Style</p>

    <div class="bush-scene" role="img" aria-label="Silhouette illustration of a stockman standing beside a large gum tree with pines and a mountain in the bush"></div>

    <p class="flavour">Honey</p>

    <div class="double-rule rule-mid"></div>
    <p class="origin">Made from 100% Australian Beef</p>
    <div class="double-rule rule-bottom"></div>
  </main>
</body>
</html>
```